KRV Business Cards

We are a local commercial development company based in Silicon Valley and we would like a new business card. I've attached a copy of our company brochure to give a flavor of what we do, our logo, info company colors/graphics, and our current business card. We don't necessarily need a crazy makeover, but would like something that feels a little bit more "fresh" and modern (we've had the same business card design for 15+ years), but still in keeping with our overall brand -- clean, high-quality, modern but timeless. Would like to add our website to the info on the card (www.velmara.com) and would like the flexibility for some folks to have an efax number listed and some not to have that included (without it looking like there is a hole).

```html
<!DOCTYPE html>
<html lang="en">
<head>
<meta charset="utf-8">
<title>KRV Business Card</title>
<link rel="stylesheet" href="https://fonts.googleapis.com/css2?family=Marcellus&family=Lora:ital@0;1&family=Lato:wght@400&display=swap">
<style>
  :root {
    --backdrop: #e9ebee;
    --brand-navy: #34506d;
    --brand-navy-light: #44627f;
    --brand-navy-dark: #2b4560;
    --accent-teal: #2a8fbd;
    --card-white: #ffffff;
    --band-grey: #bfc1c4;
    --band-grey-light: #d9dadc;
    --ink: #1c1c1c;
    --ink-soft: #3a3a3a;
    --label-blue: #5b7fa6;
  }
  html, body {
    margin: 0;
    width: 1200px;
    height: 900px;
    overflow: hidden;
    background: var(--backdrop);
  }
  .canvas {
    position: relative;
    width: 1200px;
    height: 900px;
  }
  .card {
    position: absolute;
    top: 307px;
    width: 500px;
    height: 286px;
    overflow: hidden;
    box-shadow: 0 6px 18px rgba(0,0,0,0.18);
  }
  .card--front { left: 80px; }
  .card--back { left: 620px; }
  .card svg { display: block; }
  .name { font-family: "Marcellus", serif; font-size: 21px; fill: var(--ink); letter-spacing: 1px; }
  .title { font-family: "Marcellus", serif; font-size: 12px; fill: var(--ink-soft); letter-spacing: 1.5px; }
  .address { font-family: "Lora", serif; font-size: 13px; fill: var(--ink-soft); }
  .contact { font-family: "Lato", sans-serif; font-size: 12.5px; fill: var(--ink); }
  .contact-label { fill: var(--label-blue); }
  .company { font-family: "Marcellus", serif; font-size: 27px; fill: var(--card-white); letter-spacing: 1.5px; }
  .tagline { font-family: "Lora", serif; font-style: italic; font-size: 15px; fill: #dfe7ef; }
  .website { font-family: "Marcellus", serif; font-size: 14px; fill: var(--card-white); letter-spacing: 1.5px; }
</style>
</head>
<body>
<main class="canvas">

  <section class="card card--front" aria-label="Business card front">
    <svg width="500" height="286" viewBox="0 0 500 286">
      <defs>
        <linearGradient id="greyBand" x1="0" y1="0" x2="1" y2="1">
          <stop offset="0" stop-color="var(--band-grey-light)"/>
          <stop offset="1" stop-color="var(--band-grey)"/>
        </linearGradient>
        <radialGradient id="portraitTone" cx="0.5" cy="0.45" r="0.6">
          <stop offset="0" stop-color="#d9a58c"/>
          <stop offset="0.6" stop-color="#9a6a55"/>
          <stop offset="1" stop-color="#c9a487"/>
        </radialGradient>
      </defs>
      <rect class="card-base" width="500" height="286" fill="var(--card-white)"/>
      <polygon class="header-band" points="0,0 300,0 220,58 0,112" fill="var(--brand-navy)"/>
      <polygon class="footer-band" points="0,126 100,206 500,206 500,286 0,286" fill="url(#greyBand)"/>
      <circle class="portrait-ring" cx="148" cy="72" r="66" fill="var(--card-white)"/>
      <circle class="portrait" cx="148" cy="72" r="59" fill="url(#portraitTone)" role="img" aria-label="Portrait photo of the card holder"/>

      <text class="name" x="470" y="112" text-anchor="end">DANA L WHITCOMBE</text>
      <text class="title" x="400" y="130" text-anchor="middle">PARTNER</text>
      <line class="divider" x1="236" y1="146" x2="470" y2="146" stroke="var(--accent-teal)" stroke-width="2.5" stroke-dasharray="0.1 6" stroke-linecap="round"/>
      <text class="address" x="470" y="168" text-anchor="end">212 Brookline Avenue, Palo Alto</text>
      <text class="address" x="470" y="186" text-anchor="end">California 94306</text>

      <text class="contact" x="300" y="238" text-anchor="middle"><tspan class="contact-label">Direct</tspan> 650.555.0142 | <tspan class="contact-label">Main</tspan> 650.555.0100 | <tspan class="contact-label">Fax</tspan> 650.555.0199</text>
      <text class="contact" x="300" y="259" text-anchor="middle">dana@velmara.com</text>
    </svg>
  </section>

  <section class="card card--back" aria-label="Business card back">
    <svg width="500" height="286" viewBox="0 0 500 286">
      <defs>
        <linearGradient id="navyFill" x1="0" y1="0" x2="1" y2="1">
          <stop offset="0" stop-color="var(--brand-navy-light)"/>
          <stop offset="1" stop-color="var(--brand-navy-dark)"/>
        </linearGradient>
      </defs>
      <rect class="card-base" width="500" height="286" fill="url(#navyFill)"/>
      <rect class="inner-frame" x="150" y="30" width="290" height="220" fill="none" stroke="rgba(255,255,255,0.28)" stroke-width="1"/>

      <text class="company" x="295" y="75" text-anchor="middle">KESTREL RIDGE</text>
      <text class="company" x="295" y="106" text-anchor="middle">VENTURES, LLC</text>
      <line class="separator" x1="210" y1="124" x2="380" y2="124" stroke="rgba(255,255,255,0.5)" stroke-width="1.2" stroke-dasharray="1 3"/>
      <text class="tagline" x="295" y="148" text-anchor="middle">Excellence in</text>
      <text class="tagline" x="295" y="168" text-anchor="middle">Commercial Development</text>

      <line class="rule" x1="0" y1="198" x2="198" y2="198" stroke="var(--card-white)" stroke-width="2"/>
      <text class="website" x="295" y="203" text-anchor="middle">WWW.VELMARA.COM</text>
      <line class="rule" x1="392" y1="198" x2="500" y2="198" stroke="var(--card-white)" stroke-width="2"/>
    </svg>
  </section>

</main>
</body>
</html>
```